I need bigcommerce design template

hi, am looking for a quality, professional, attractive and mature bigcommerce template for my site. My site will sell clothes and bags and shoes. Basically what you are to do is setup the store. I have domain name which hostwren will attach them self.

```html
<!DOCTYPE html>
<html lang="en">
<head>
<meta charset="utf-8">
<title>Marco Valenti – Store</title>
<link rel="stylesheet" href="https://fonts.googleapis.com/css2?family=Roboto:wght@300;400;500;700;900&display=swap">
<style>
:root{
  --black:#000;
  --ink:#222;
  --text:#333;
  --muted:#555;
  --white:#fff;
  --green:#3aa935;
  --grey-btn:#8a8a8a;
  --dark-btn:#3a3a3a;
  --footer:#1d1d1d;
  --footer-bottom:#161616;
  --orange:#f7941d;
  --teal:#0fa58c;
  --pink:#e8388f;
}
*{box-sizing:border-box;margin:0;padding:0}
html,body{width:853px;height:1200px;overflow:hidden;background:var(--white);font-family:"Roboto",sans-serif;color:var(--text)}
.page{position:relative;width:853px;height:1200px}
.header{position:absolute;left:0;top:0;width:853px;height:158px;background:var(--black)}
.logo{position:absolute;left:92px;top:40px;color:var(--white);font:300 30px/1 "Roboto",sans-serif;letter-spacing:.5px}
.search{position:absolute;left:455px;top:19px;width:228px;height:17px;display:flex}
.search-input{flex:1;background:#2a2a2a;color:#777;font-size:7px;line-height:17px;padding-left:6px}
.search-btn{width:54px;background:var(--green);color:var(--white);font-size:8px;line-height:17px;text-align:center}
.cart{position:absolute;left:694px;top:20px;color:var(--white);font-size:8px;display:flex;align-items:center;gap:4px}
.nav{position:absolute;right:92px;top:59px;display:flex;gap:23px}
.nav a{color:var(--white);text-decoration:none;font-size:10px;font-weight:500}
.hero{position:absolute;left:91px;top:94px;width:671px;height:396px;overflow:hidden}
.hero-photo{position:absolute;inset:0;background:linear-gradient(120deg,#6f7c85 0%,#4d5358 40%,#3a3a3a 70%,#7d8a92 100%)}
.hero svg.shapes{position:absolute;inset:0}
.hero-copy{position:absolute;left:420px;top:164px;width:300px;text-align:left;color:var(--white)}
.hero-kicker{font-size:15px;font-weight:300;position:absolute;left:0;top:0}
.hero-title{font-size:44px;font-weight:900;position:absolute;left:-6px;top:16px;letter-spacing:-1px}
.hero-btn{position:absolute;left:-6px;top:66px;width:87px;height:24px;background:var(--grey-btn);color:var(--white);font-size:8px;line-height:24px;text-align:center}
.arrow{position:absolute;top:190px}
.tiles{position:absolute;left:91px;top:504px;width:671px;height:159px}
.tile{position:absolute;top:0;width:212px;height:159px;overflow:hidden}
.tile-photo{position:absolute;inset:0}
.tile-box{position:absolute;left:39px;top:48px;width:128px;height:77px;background:rgba(20,20,20,.92);color:var(--white);text-align:center}
.tile-kicker{font-size:14px;font-weight:300;margin-top:14px}
.tile-title{font-size:25px;font-weight:900;letter-spacing:-1px;line-height:1;margin-top:2px}
.tile-btn{position:absolute;left:28px;top:63px;width:72px;height:17px;font-size:6px;font-weight:700;line-height:17px;clip-path:polygon(0 0,100% 0,88% 100%,12% 100%)}
.section-title{position:absolute;left:0;width:853px;top:708px;text-align:center;font-size:22px;font-weight:500;color:var(--ink)}
.product{position:absolute;top:759px;width:155px}
.product-photo{width:155px;height:124px}
.product-name{margin-top:13px;font-size:10.5px;color:var(--text)}
.product-price{margin-top:4px;font-size:7.5px;color:var(--text)}
.product-btn{margin-top:9px;width:70px;height:22px;background:var(--dark-btn);color:var(--white);font-size:8px;line-height:22px;text-align:center}
.footer{position:absolute;left:0;top:984px;width:853px;height:216px;background:var(--footer);color:#ddd}
.foot-col{position:absolute;top:27px;font-size:8px}
.foot-col h4{font-size:8px;font-weight:500;color:var(--white);margin-bottom:20px}
.foot-col li{list-style:none;line-height:14px}
.foot-bottom{position:absolute;left:0;top:167px;width:853px;height:49px;background:var(--footer-bottom);font-size:8px;color:#ddd}
.fb{position:absolute;top:0;line-height:8px}
.social{position:absolute;left:423px;top:14px;display:flex;gap:6px}
.social span{width:17px;height:17px;border-radius:50%;background:#888}
.cards{position:absolute;left:622px;top:15px;display:flex;gap:3px}
.cards span{width:26px;height:16px;background:#e8e8e8;border-radius:1px}
</style>
</head>
<body>
<div class="page">
  <header class="header">
    <div class="logo">Marco Valenti</div>
    <div class="search"><div class="search-input">Search Your Products</div><div class="search-btn">SEARCH</div></div>
    <div class="cart">
      <svg width="16" height="14" viewBox="0 0 16 14"><path d="M1 1h3l2 8h8l1.5-6H5" fill="none" stroke="#bbb" stroke-width="1.2"/><circle cx="7" cy="12" r="1.2" fill="#bbb"/><circle cx="13" cy="12" r="1.2" fill="#bbb"/></svg>
      Cart: 0 items
    </div>
    <nav class="nav"><a href="#">HOME</a><a href="#">ABOUT US</a><a href="#">PRODUCTS</a><a href="#">NEW ARRIVALS</a><a href="#">COLLECTIONS</a><a href="#">CONTACT US</a></nav>
  </header>

  <section class="hero">
    <div class="hero-photo" role="img" aria-label="Photo of a man in a dark jacket sitting on a pier with a leather travel bag"></div>
    <svg class="shapes" width="671" height="396" viewBox="0 0 671 396">
      <polygon points="310,0 470,0 390,396 310,396 390,0" fill="#111" opacity="0"/>
      <polygon points="309,0 630,0 470,396 309,396 470,0" fill="none"/>
      <polygon points="310,0 470,396 310,396" fill="#0f0f0f" opacity=".9"/>
      <polygon points="320,0 630,0 470,396" fill="#151515" opacity=".85"/>
      <polygon points="470,396 630,0 625,396" fill="#0f0f0f" opacity=".75"/>
    </svg>
    <div class="hero-copy">
      <div class="hero-kicker">Marco Valenti</div>
      <div class="hero-title">BAGS</div>
      <div class="hero-btn">SHOP NOW</div>
    </div>
    <svg class="arrow" style="left:25px" width="12" height="18" viewBox="0 0 12 18"><path d="M10 2L3 9l7 7" fill="none" stroke="#fff" stroke-width="2"/></svg>
    <svg class="arrow" style="left:634px" width="12" height="18" viewBox="0 0 12 18"><path d="M2 2l7 7-7 7" fill="none" stroke="#fff" stroke-width="2"/></svg>
  </section>

  <section class="tiles">
    <div class="tile" style="left:0">
      <div class="tile-photo" role="img" aria-label="Photo of a woman with a bag on a city street" style="background:linear-gradient(135deg,#8fb6c2,#b79a6e 60%,#4a6a6a)"></div>
      <div class="tile-box"><div class="tile-kicker">Marco Valenti</div><div class="tile-title">BAGS</div><div class="tile-btn" style="background:var(--orange)">SHOP NOW</div></div>
    </div>
    <div class="tile" style="left:230px">
      <div class="tile-photo" role="img" aria-label="Photo of a man in a striped sweater" style="background:linear-gradient(135deg,#d9d9d9,#f1f1f1 60%,#c9c9c9)"></div>
      <div class="tile-box"><div class="tile-kicker">Marco Valenti</div><div class="tile-title">CLOTHES</div><div class="tile-btn" style="background:var(--teal)">SHOP NOW</div></div>
    </div>
    <div class="tile" style="left:459px">
      <div class="tile-photo" role="img" aria-label="Photo of legs in jeans and heels on a paved square" style="background:linear-gradient(135deg,#cfcac4,#b9b3ad 60%,#d8d4cf)"></div>
      <div class="tile-box"><div class="tile-kicker">Marco Valenti</div><div class="tile-title">SHOES</div><div class="tile-btn" style="background:var(--pink)">SHOP NOW</div></div>
    </div>
  </section>

  <h2 class="section-title">OUR PRODUCTS</h2>

  <div class="product" style="left:91px"><div class="product-photo" role="img" aria-label="Photo of leather loafers on dark stones" style="background:linear-gradient(135deg,#2a2a2a,#5b6f84 50%,#1c1c1c)"></div><div class="product-name">Neque porro quisquam</div><div class="product-price">$19.99</div><div class="product-btn">ADD TO CART</div></div>
  <div class="product" style="left:263px"><div class="product-photo" role="img" aria-label="Photo of a brown leather handbag" style="background:linear-gradient(135deg,#9fd0c0,#b4582d 50%,#1d2a4a)"></div><div class="product-name">Neque porro quisquam</div><div class="product-price">$19.99</div><div class="product-btn">ADD TO CART</div></div>
  <div class="product" style="left:435px"><div class="product-photo" role="img" aria-label="Photo of a woman in a red top outdoors" style="background:linear-gradient(135deg,#a7b68a,#e8e2d2 50%,#d85444)"></div><div class="product-name">Neque porro quisquam</div><div class="product-price">$19.99</div><div class="product-btn">ADD TO CART</div></div>
  <div class="product" style="left:607px"><div class="product-photo" role="img" aria-label="Photo of a red quilted handbag" style="background:linear-gradient(135deg,#2a0a0a,#b3141b 55%,#6d0c10)"></div><div class="product-name">Neque porro quisquam</div><div class="product-price">$19.99</div><div class="product-btn">ADD TO CART</div></div>

  <footer class="footer">
    <div class="foot-col" style="left:91px"><h4>Menu</h4><ul><li>Home</li><li>About us</li><li>Products</li><li>New Arrivals</li><li>Collections</li><li>Contact Us</li></ul></div>
    <div class="foot-col" style="left:262px"><h4>Our Offers</h4><ul><li>New products</li><li>Specials</li><li>Manufacturers</li><li>Suppliers</li><li>Shipping &amp; Returns</li></ul></div>
    <div class="foot-col" style="left:434px"><h4>Your Account</h4><ul><li>Log in</li><li>Create an Account</li></ul></div>
    <div class="foot-col" style="left:607px"><h4>Contact Us</h4><ul><li>Atelier Nordlicht</li><li>Lindenweg 42b</li><li>20148 Hamburg</li><li>Germany</li><li>Telephone: +49 40 55512840</li><li>E-mail: hello@ateliernordlicht.com</li></ul></div>
    <div class="foot-bottom">
      <div class="fb" style="left:91px;top:20px">© 2015 Privacy Notice &nbsp;| &nbsp;Conditions of Use</div>
      <div class="fb" style="left:339px;top:20px">Connect With Us</div>
      <div class="social"><span></span><span></span><span></span><span></span></div>
      <div class="fb" style="left:527px;top:19px">Payment Options</div>
      <div class="cards"><span></span><span></span><span></span><span></span><span></span></div>
    </div>
  </footer>
</div>
</body>
</html>
```